Steadfast MD - Sleep Medicine Specialist - Business Cards

We are a new medical practice called Steadfast MD. We are sleep medicine specialists and we will be conducting sleep studies on patients with sleep related ailments. We want the business card to be bold, professional, and clean with the logo as the stand out visual piece. We dont like wild flashy designs. We want our design to be bold and classic while at the same time conveying who we are and what we do. We are reliable, professional, and the best in the business.

Industry/Entity Type

Health Care

Contact Information for Business Card

- Clean
- Bold
- Classic
- not cluttered

Requirements
Must have
• logo, website, phone number
Nice to have
• several options to choose from
Should not have
• flashy imaged - reflective print - images of people sleeping

```html
<!DOCTYPE html>
<html lang="en">
<head>
<meta charset="UTF-8">
<title>Steadfast MD — Business Cards</title>
<link href="https://fonts.googleapis.com/css2?family=Montserrat:wght@400;500;800&display=swap" rel="stylesheet">
<style>
  :root {
    --brand-red: #e81f27;
    --ink: #111111;
    --paper: #ffffff;
    --stage: #2a2a2a;
    --muted: #333333;
  }
  * { box-sizing: border-box; margin: 0; padding: 0; }
  html, body { width: 1200px; height: 900px; overflow: hidden; }
  body {
    background: var(--stage);
    font-family: "Montserrat", Arial, sans-serif;
    position: relative;
  }
  .card {
    position: absolute;
    width: 500px;
    height: 286px;
    border-radius: 18px;
    overflow: hidden;
  }
  .card-front {
    left: 120px; top: 120px;
    background: var(--brand-red);
    display: flex; align-items: center; justify-content: center;
  }
  .card-back {
    left: 580px; top: 494px;
    background: var(--paper);
  }
  .brand-lockup { display: flex; align-items: center; gap: 12px; }
  .brand-dot {
    width: 62px; height: 62px; border-radius: 50%;
    border: 5px solid currentColor;
  }
  .brand-name {
    font-weight: 800; font-size: 40px; letter-spacing: -1px;
  }
  .card-front .brand-lockup { color: var(--paper); }
  .card-back .brand-lockup {
    color: var(--ink);
    position: absolute; left: 70px; top: 40px;
  }
  .card-back .brand-dot { color: var(--brand-red); width: 66px; height: 66px; }
  .card-back .brand-name { font-size: 38px; }
  .holder {
    position: absolute; left: 70px; top: 138px; width: 170px; text-align: right;
  }
  .holder-name {
    color: var(--brand-red); font-weight: 800; font-size: 17px; letter-spacing: 0.3px;
  }
  .holder-role { color: var(--ink); font-weight: 500; font-size: 12px; margin-top: 2px; }
  .divider {
    position: absolute; left: 258px; top: 128px; width: 1.5px; height: 52px; background: var(--ink);
  }
  .contact-list {
    position: absolute; left: 274px; top: 126px; list-style: none;
  }
  .contact-list li {
    display: flex; align-items: center; gap: 7px;
    font-size: 11.5px; color: var(--muted); line-height: 19px;
  }
  .contact-list svg { width: 11px; height: 11px; fill: var(--brand-red); flex: none; }
  .address {
    position: absolute; left: 0; right: 0; top: 232px;
    text-align: center; font-size: 11.5px; color: var(--muted);
  }
</style>
</head>
<body>
  <section class="card card-front">
    <div class="brand-lockup">
      <span class="brand-dot"></span>
      <span class="brand-name">Steadfast MD</span>
    </div>
  </section>

  <section class="card card-back">
    <div class="brand-lockup">
      <span class="brand-dot"></span>
      <span class="brand-name">Steadfast MD</span>
    </div>

    <div class="holder">
      <p class="holder-name">DANIEL HART</p>
      <p class="holder-role">Manager</p>
    </div>

    <span class="divider"></span>

    <ul class="contact-list">
      <li>
        <svg viewBox="0 0 24 24" aria-hidden="true"><path d="M6.6 10.8a15 15 0 0 0 6.6 6.6l2.2-2.2a1 1 0 0 1 1-.25 11.4 11.4 0 0 0 3.6.57 1 1 0 0 1 1 1V20a1 1 0 0 1-1 1A17 17 0 0 1 3 4a1 1 0 0 1 1-1h3.5a1 1 0 0 1 1 1c0 1.25.2 2.45.57 3.6a1 1 0 0 1-.25 1z"/></svg>
        (555) 014 - 2270
      </li>
      <li>
        <svg viewBox="0 0 24 24" aria-hidden="true"><path d="M2 5h20v14H2z M2 5l10 8 10-8" fill-rule="evenodd"/></svg>
        info@steadfastmd.com
      </li>
      <li>
        <svg viewBox="0 0 24 24" aria-hidden="true"><circle cx="12" cy="12" r="10"/></svg>
        www.steadfastmd.com
      </li>
    </ul>

    <p class="address">412 N. Maple Ave. Country name , MN 50123</p>
  </section>
</body>
</html>
```